I would like a stylish low key card that represents my Fern Lodge. A boutique rental property . This property is of the highest standard and I wish the card to covey this without being old fashion

Industry/Entity Type

Boutique

Contact Information for Business Card

Tess Varlow
0427350918
tess.varlow@varlow.com.au Fern Lodge

```html
<!DOCTYPE html>
<html lang="en">
<head>
<meta charset="utf-8">
<title>Fern Lodge — Tess Varlow</title>
<link rel="stylesheet" href="https://fonts.googleapis.com/css2?family=Didact+Gothic&display=swap">
<style>
  :root {
    --backdrop: #d9d9d9;
    --card: #ffffff;
    --ink: #111111;
    --ink-soft: #2a2a2a;
    --ornament-dark: #1a1a1a;
    --ornament-light: #4a4a4a;
    --paper-text: #ffffff;
  }
  * { margin: 0; padding: 0; box-sizing: border-box; }
  html, body {
    width: 1200px;
    height: 900px;
    overflow: hidden;
    background: var(--backdrop);
  }
  .business-card {
    position: absolute;
    left: 180px;
    top: 210px;
    width: 840px;
    height: 480px;
    background: var(--card);
    box-shadow: 0 10px 30px rgba(0,0,0,0.18);
    font-family: "Didact Gothic", "Century Gothic", sans-serif;
    color: var(--ink);
    overflow: hidden;
  }
  .ornament {
    position: absolute;
    border-radius: 40px;
    background: linear-gradient(135deg, var(--ornament-dark), var(--ornament-light));
  }
  .ornament--top-left {
    left: 190px;
    top: 30px;
    width: 150px;
    height: 34px;
  }
  .ornament--right {
    left: 712px;
    top: 104px;
    width: 92px;
    height: 104px;
    border-radius: 30px;
  }
  .brand {
    position: absolute;
    left: 0;
    right: 0;
    top: 112px;
    display: flex;
    justify-content: center;
    align-items: center;
    gap: 14px;
    padding-left: 60px;
  }
  .brand__mark {
    width: 22px;
    height: 22px;
    background: var(--ink);
  }
  .brand__name {
    font-size: 38px;
    letter-spacing: 2px;
    color: var(--ink);
  }
  .name-banner {
    position: absolute;
    left: 0;
    top: 0;
    width: 840px;
    height: 480px;
  }
  .name-banner__ribbon { fill: var(--ink); }
  .name-banner__text {
    font-family: "Didact Gothic", "Century Gothic", sans-serif;
    font-size: 38px;
    letter-spacing: 3px;
    fill: var(--paper-text);
  }
  .contact {
    position: absolute;
    left: 62px;
    top: 360px;
    font-size: 21px;
    line-height: 1.55;
    color: var(--ink-soft);
    list-style: none;
    text-align: right;
  }
</style>
</head>
<body>
  <article class="business-card">
    <div class="ornament ornament--top-left" role="img" aria-label="Black flourish scroll ornament"></div>
    <div class="ornament ornament--right" role="img" aria-label="Black flourish scroll ornament"></div>

    <div class="brand">
      <span class="brand__mark"></span>
      <span class="brand__name">Fern Lodge</span>
    </div>

    <svg class="name-banner" viewBox="0 0 840 480">
      <path class="name-banner__ribbon"
        d="M150,228 Q465,200 780,252 L758,286 L786,320 Q465,274 150,296 L174,262 Z"/>
      <path id="banner-baseline" d="M200,278 Q465,250 740,294" fill="none"/>
      <text class="name-banner__text" text-anchor="middle">
        <textPath href="#banner-baseline" startOffset="50%">TESS VARLOW</textPath>
      </text>
    </svg>

    <ul class="contact">
      <li class="contact__phone">0427350918</li>
      <li class="contact__email">tess.varlow@varlow.com.au</li>
    </ul>
  </article>
</body>
</html>
```